Business card and stationery design

Harbour & Summit Planners is a leading event and conference design and management company.
Please view harbourandsummit.com.au

The business cards needs to convey:
- professionalism and competency
- exclusivity
- memorable experiences and quality

The business card needs to have the following aspects:
- double sided
- Full colour CMYK
- Printed on either high gloss matt card (designer to recommend)

For the business stationery we require:
- Letterhead with top banner and bottom footer
- A thank you card design
- a with compliments slip design
- a MS powerpoint and MS publisher client presentation slide design which includes cover page and then a standard presentation page
(Note- we do NOT require an envelope design- who sends letters these days!)

The company image is using the key colours of gold, silver and black.
A black background to the business card has been used before and is preferred although we are open to options.

Target Market(s)

High end corporations and businesses that require their events and conferences to be exceptionally well designed and managed

Industry/Entity Type

Business

Contact Information for Business Card

FRONT:

Darcy Whitlam
- Event and Conference Specialist

Mobile- +61 (0) 491 362 047
Office- 1300 586 917
darcyw@harbourandsummit.com.au

Web- harbourandsummit.com.au

BACK:

- Event and

Font styles to use
Other font styles liked:
• The logo designer used Trajan Pro Bold 3 for the font text in the logo

Requirements
Must have
• Amazing design of the following:
• - business card (double sided)
• - letterhead
• - client thank you card
• - powerpoint and publisher client presentation design files

```html
<!DOCTYPE html>
<html lang="en">
<head>
<meta charset="utf-8">
<title>Harbour &amp; Summit Planners – Business Card</title>
<link rel="stylesheet" href="https://fonts.googleapis.com/css2?family=Cinzel:wght@600&family=Josefin+Sans:wght@400;700&display=swap">
<style>
  :root {
    --backdrop: #1c1c1c;
    --card-black: #0b0b0b;
    --card-white: #ffffff;
    --ink: #111111;
    --silver: #c9c9c9;
    --gold: #c9a94a;
    --rule: #9a9a9a;
  }
  * { margin: 0; padding: 0; box-sizing: border-box; }
  html, body { width: 1200px; height: 969px; overflow: hidden; }
  body {
    background: var(--backdrop);
    font-family: "Josefin Sans", sans-serif;
    position: relative;
  }
  .card {
    position: absolute;
    left: 300px;
    width: 600px;
    height: 343px;
    border-radius: 22px;
  }
  .card-back {
    top: 110px;
    background: radial-gradient(ellipse at 55% 40%, #2a2a2a 0%, var(--card-black) 70%);
    display: flex;
    flex-direction: column;
    align-items: center;
    justify-content: center;
    gap: 26px;
  }
  .card-back .brand-name {
    font-family: "Cinzel", serif;
    font-weight: 600;
    font-size: 30px;
    letter-spacing: 1px;
    color: var(--silver);
  }
  .card-back .web {
    font-size: 17px;
    letter-spacing: 0.5px;
    color: var(--gold);
  }
  .card-front {
    top: 516px;
    background: var(--card-white);
    display: flex;
    align-items: center;
  }
  .card-front .brand-name {
    width: 290px;
    text-align: center;
    font-family: "Cinzel", serif;
    font-weight: 600;
    font-size: 21px;
    line-height: 1.3;
    color: var(--ink);
  }
  .divider {
    width: 1px;
    height: 170px;
    background: linear-gradient(to bottom, transparent, var(--rule) 30%, var(--rule) 70%, transparent);
  }
  .contact { padding-left: 28px; color: var(--ink); }
  .contact .person {
    font-weight: 700;
    font-size: 19px;
    letter-spacing: 0.5px;
    text-transform: uppercase;
  }
  .contact .role { font-size: 16px; margin-bottom: 14px; }
  .contact ul { list-style: none; }
  .contact li {
    display: flex;
    align-items: center;
    gap: 10px;
    font-size: 15px;
    line-height: 24px;
  }
  .contact svg { width: 14px; height: 14px; fill: var(--ink); flex: none; }
</style>
</head>
<body>
  <section class="card card-back" aria-label="Card back">
    <div class="brand-name">Harbour &amp; Summit Planners</div>
    <div class="web">www.harbourandsummit.com.au</div>
  </section>

  <section class="card card-front" aria-label="Card front">
    <div class="brand-name">Harbour &amp; Summit<br>Planners</div>
    <div class="divider"></div>
    <div class="contact">
      <div class="person">Darcy Whitlam</div>
      <div class="role">Event and Conference Specialist</div>
      <ul>
        <li>
          <svg viewBox="0 0 14 14" aria-hidden="true"><path d="M4 0h6a1 1 0 0 1 1 1v12a1 1 0 0 1-1 1H4a1 1 0 0 1-1-1V1a1 1 0 0 1 1-1zm0.5 1.5v10h5v-10z"/></svg>
          +61 (0) 491 362 047
        </li>
        <li>
          <svg viewBox="0 0 14 14" aria-hidden="true"><path d="M1 4c2-3 10-3 12 0l-1 2-3-1V4H5v1L2 6zM3 7h8l2 6H1z"/></svg>
          1300 586 917
        </li>
        <li>
          <svg viewBox="0 0 14 14" aria-hidden="true"><path d="M0 3h14v8H0zm1 1l6 4 6-4z"/></svg>
          darcyw@harbourandsummit.com.au
        </li>
        <li>
          <svg viewBox="0 0 14 14" aria-hidden="true"><path d="M7 0a7 7 0 1 0 0 14A7 7 0 0 0 7 0zm0 1.2c.9 0 1.8 2.2 2 5.2H5c.2-3 1.1-5.2 2-5.2zM1.2 7.6H3.8c.1 2 .6 3.7 1.3 4.8a5.8 5.8 0 0 1-3.9-4.8zm0-1.2a5.8 5.8 0 0 1 3.9-4.8C4.4 2.7 3.9 4.4 3.8 6.4zm3.8 1.2h4c-.2 3-1.1 5.2-2 5.2s-1.8-2.2-2-5.2zm5.2 0h2.6a5.8 5.8 0 0 1-3.9 4.8c.7-1.1 1.2-2.8 1.3-4.8zm0-1.2c-.1-2-.6-3.7-1.3-4.8a5.8 5.8 0 0 1 3.9 4.8z"/></svg>
          www.harbourandsummit.com.au
        </li>
      </ul>
    </div>
  </section>
</body>
</html>
```